Riverstone & Pine Construction and Developments business cards

A business card with watermark background (construction work)

Company logo attached

Home improvement projects
House renovations
Bathroom and kitchen renovations
House extensions
New builds and granny flats

Director Omar Haddine
(Phone number)
omar@rpcbuildgroup.com.au
(Instagram logo) rpc_buildgroup

```html
<!DOCTYPE html>
<html lang="en">
<head>
<meta charset="utf-8">
<title>Riverstone &amp; Pine Construction and Developments – Business Cards</title>
<link rel="stylesheet" href="https://fonts.googleapis.com/css2?family=Raleway:wght@600;700&family=Open+Sans:wght@400&display=swap">
<style>
  :root {
    --stage: #0e0e0e;
    --paper: #ffffff;
    --brand-blue: #2f73b5;
    --ink: #3a3a3a;
    --bullet: #444444;
    --mark-tint: #3ec0c9;
  }
  * { margin: 0; padding: 0; box-sizing: border-box; }
  html, body {
    width: 1134px; height: 1200px; overflow: hidden;
    background: var(--stage);
  }
  .card {
    position: absolute; left: 235px; width: 663px; height: 394px;
    box-shadow: 3px 4px 6px rgba(0,0,0,.6);
    overflow: hidden;
  }
  .card-front { top: 189px; background: var(--paper); }
  .card-back  { top: 636px; background: var(--brand-blue); }
  .front-band {
    position: absolute; left: 0; right: 0; bottom: 0; height: 9px;
    background: var(--brand-blue);
  }
  .holder { position: absolute; left: 34px; top: 60px; }
  .holder-name {
    font: 700 26px/1 "Raleway", sans-serif; color: var(--brand-blue);
  }
  .holder-role {
    margin-top: 5px; font: 400 16px/1 "Open Sans", sans-serif; color: var(--ink);
  }
  .brand-name {
    position: absolute; font-family: "Raleway", sans-serif; font-weight: 700;
    text-align: center; line-height: 1.15;
  }
  .card-front .brand-name {
    left: 405px; top: 118px; width: 236px; font-size: 24px; color: var(--brand-blue);
  }
  .card-back .brand-name {
    left: 150px; top: 210px; width: 363px; font-size: 32px; color: var(--mark-tint);
  }
  .brand-name .brand-sub { display: block; font-size: .58em; letter-spacing: .03em; margin-top: 6px; }
  .contact {
    position: absolute; left: 34px; font: 400 16px/20px "Open Sans", sans-serif; color: var(--ink);
    display: flex; align-items: center; gap: 5px; white-space: nowrap;
  }
  .contact svg { width: 18px; height: 18px; flex: none; }
  .contact .accent { color: var(--brand-blue); }
  .contact-social { top: 242px; font-size: 17px; }
  .contact-phone  { top: 295px; }
  .contact-mail   { top: 318px; }
  .contact-web    { top: 341px; }
  .services {
    position: absolute; right: 26px; top: 245px; list-style: none; text-align: right;
    font: 400 16px/23.4px "Open Sans", sans-serif; color: var(--brand-blue);
    white-space: nowrap;
  }
  .services li::after {
    content: ""; display: inline-block; width: 9px; height: 9px; margin-left: 6px;
    background: var(--bullet); vertical-align: 1px;
  }
</style>
</head>
<body>
  <section class="card card-front">
    <div class="holder">
      <div class="holder-name">Omar Haddine</div>
      <div class="holder-role">Director</div>
    </div>

    <div class="brand-name">Riverstone &amp; Pine<span class="brand-sub">Construction and Developments</span></div>

    <div class="contact contact-social">
      <svg viewBox="0 0 18 18"><rect x="1" y="1" width="16" height="16" rx="3" fill="#2f73b5"/></svg>
      rpc_buildgroup
    </div>
    <div class="contact contact-phone">
      <svg viewBox="0 0 18 18"><path d="M4 2l3 3-2 2c1 2 3 4 5 5l2-2 3 3-2 3C7 16 2 11 1 5z" fill="none" stroke="#2f73b5" stroke-width="1.6" stroke-linejoin="round"/></svg>
      044-987 654 321
    </div>
    <div class="contact contact-mail">
      <svg viewBox="0 0 18 18"><rect x="1" y="4" width="16" height="11" fill="#2f73b5"/><path d="M1 4l8 6 8-6" fill="none" stroke="#fff" stroke-width="1.3"/></svg>
      omar@rpcbuildgroup.com.au
    </div>
    <div class="contact contact-web">
      <svg viewBox="0 0 18 18" fill="none" stroke="#2f73b5" stroke-width="1.4"><circle cx="9" cy="9" r="7.5"/><ellipse cx="9" cy="9" rx="3.2" ry="7.5"/><path d="M1.5 9h15M3 5h12M3 13h12"/></svg>
      <span>www.<span class="accent">rpcbuildgroup</span>.com.au</span>
    </div>

    <ul class="services">
      <li>Home improvement projects</li>
      <li>House renovations</li>
      <li>Bathroom and kitchen renovations</li>
      <li>House extensions</li>
      <li>New builds and granny flats</li>
    </ul>

    <div class="front-band"></div>
  </section>

  <section class="card card-back">
    <div class="brand-name">Riverstone &amp; Pine<span class="brand-sub">Construction and Developments</span></div>
  </section>
</body>
</html>
```